Home Staging Company needs business card design

We're a home staging company called Brightly Settled Home Staging. We would like a business card design that includes aqua and gray. Our current logo of house within chair is fine but I find we almost always use the logo in one color. I'll upload images of front and back of our current card and our logo. Note that we have dropped "Solutions" from our company name and don't want to include it on the card.

Target Market(s)

Realtors and homeowners - people interested in selling their homes

Contact Information for Business Card

Marisol Vantrease
Brightly Settled Home Staging
612-348-9071
www.brightlysettled.example
marisol@brightlysettled.example

Font styles to use
Serif
Script

Requirements
Must have
• My logo and contact details
• UPDATE***
• I forgot to say that the company name should be included on the front of the card somehow.

```html
<!DOCTYPE html>
<html lang="en">
<head>
<meta charset="utf-8">
<title>Brightly Settled Home Staging – Business Cards</title>
<link href="https://fonts.googleapis.com/css2?family=Playfair+Display:wght@400&family=Playfair+Display+SC:wght@400&family=Questrial&display=swap" rel="stylesheet">
<style>
  :root {
    --backdrop: #eceae6;
    --aqua: #2ba6b2;
    --charcoal: #2e2e2f;
    --white: #ffffff;
    --soft-white: #e9e9e9;
  }
  * { margin: 0; padding: 0; box-sizing: border-box; }
  html, body {
    width: 1200px;
    height: 870px;
    overflow: hidden;
    background: var(--backdrop);
  }
  .canvas {
    position: relative;
    width: 1200px;
    height: 870px;
  }
  .card {
    position: absolute;
    width: 560px;
    height: 320px;
    border-radius: 22px;
    box-shadow: 0 10px 28px rgba(0, 0, 0, 0.18);
    display: flex;
    flex-direction: column;
    align-items: center;
    color: var(--white);
  }
  .card--front {
    left: 70px;
    top: 70px;
    background: var(--aqua);
    justify-content: center;
  }
  .card--back {
    left: 570px;
    top: 480px;
    background: var(--charcoal);
    padding-top: 52px;
  }
  .brand {
    display: flex;
    align-items: center;
    gap: 16px;
  }
  .brand__dot {
    width: 54px;
    height: 54px;
    border-radius: 50%;
    background: var(--white);
    flex: none;
  }
  .brand__name {
    font-family: "Playfair Display", serif;
    font-weight: 400;
    line-height: 1;
    color: var(--white);
  }
  .card--front .brand__name { font-size: 46px; }
  .card--back .brand__dot { width: 40px; height: 40px; }
  .card--back .brand__name { font-size: 34px; }
  .brand__tagline {
    font-family: "Playfair Display", serif;
    font-size: 12px;
    letter-spacing: 4px;
    text-transform: uppercase;
    margin-top: 6px;
    text-align: right;
  }
  .card--front .website {
    position: absolute;
    bottom: 54px;
    font-family: "Questrial", sans-serif;
    font-size: 15px;
    letter-spacing: 0.5px;
  }
  .holder-name {
    font-family: "Playfair Display SC", serif;
    font-size: 24px;
    letter-spacing: 1.5px;
    margin-top: 34px;
  }
  .contact {
    list-style: none;
    margin-top: 18px;
    text-align: center;
    font-family: "Questrial", sans-serif;
    font-size: 15px;
    line-height: 1.3;
    color: var(--soft-white);
  }
  .social {
    display: flex;
    gap: 14px;
    margin-top: 18px;
  }
  .social__dot {
    width: 11px;
    height: 11px;
    border-radius: 50%;
    background: var(--soft-white);
  }
</style>
</head>
<body>
<main class="canvas">
  <section class="card card--front" aria-label="Business card front">
    <div class="brand">
      <span class="brand__dot"></span>
      <div>
        <div class="brand__name">Brightly Settled</div>
        <div class="brand__tagline">Home Staging</div>
      </div>
    </div>
    <p class="website">www.brightlysettled.example</p>
  </section>

  <section class="card card--back" aria-label="Business card back">
    <div class="brand">
      <span class="brand__dot"></span>
      <div>
        <div class="brand__name">Brightly Settled</div>
        <div class="brand__tagline">Home Staging</div>
      </div>
    </div>
    <h1 class="holder-name">Marisol Vantrease</h1>
    <ul class="contact">
      <li>612-348-9071</li>
      <li>marisol@brightlysettled.example</li>
      <li>www.brightlysettled.example</li>
    </ul>
    <div class="social" aria-label="Social media links">
      <span class="social__dot"></span>
      <span class="social__dot"></span>
      <span class="social__dot"></span>
    </div>
  </section>
</main>
</body>
</html>
```